Infographic from a blog post about Reliability Centred Maintenance (RCM)

I need someone to convert a detailed blog post into an Infographic. The post is here: https://www.steadyplantworks.com/reliability-centered-maintenance-principles/

The infographic should include:
(1) the history of RCM, probably best done by using the 1st, 2nd and 3rd generation of maintenance concepts as discussed in the article. For the 3rd generation includesome of the metrics that show the difference RCM made e.g. the comparison between the maintenance of a KV-3 versus that of the 528-400

(2) All the 9 principles that are mentioned in the article with a large part of the infographic dedicated to Principle #2 with the failure patterns and distributions

For the infographic make sure it fits with the design & branding of the overall site www.steadyplantworks.com

Industry/Entity Type

Industrial

Font styles to use
Other font styles liked:
• roboto condensed bold for titles, raleway for text

Colors
0292cd
333333
ffc214

Requirements
Must have
• The infographic must include:
• (1) the history of RCM and some of the metrics that show the difference RCM made e.g. the comparison between the maintenance of a KV-3 versus that of the 528-400
• (2) All the 9 principles that are mentioned in the article with a large part of the infographic dedicated to Principle #2 with the failure patterns and distributions
• Use following main colours:
• #3C3C3C
• #0187AC
• Use the following colors for highlights:
• #079F6D
• #B91449
• #FFC000
Nice to have
• For the history section use some imagery along these lines:
• 1st generation of maintenance = industrial revolution so steam train, steam equipment
• 2nd generation of maintenance = from world war 2, maybe show a tank
• 3rd generation of maintenance = developed by aviation so show a picture of a 528-400 airplane

```html
<!DOCTYPE html>
<html lang="en">
<head>
<meta charset="utf-8">
<title>Reliability Centered Maintenance Principles</title>
<link href="https://fonts.googleapis.com/css2?family=Roboto+Condensed:wght@400;700&family=Raleway:wght@400;500;600&display=swap" rel="stylesheet">
<style>
  :root{
    --bg:#0a86ad;
    --panel:#f4f4f4;
    --ink:#3c3c3c;
    --blue:#0187ac;
    --green:#079f6d;
    --crimson:#b91449;
    --gold:#ffc000;
    --rule:#9a9a9a;
  }
  *{margin:0;padding:0;box-sizing:border-box}
  html,body{width:1200px;height:776px;overflow:hidden}
  body{background:var(--bg);position:relative;font-family:"Raleway",sans-serif;color:var(--ink)}
  .abs{position:absolute}
  .brand{position:absolute;width:74px;height:54px;display:flex;flex-direction:column;justify-content:center;
    font-family:"Raleway",sans-serif;font-weight:600;color:#fff;font-size:11px;line-height:13px;text-transform:uppercase;letter-spacing:.5px}
  .page-title{position:absolute;font-family:"Roboto Condensed",sans-serif;font-weight:700;color:#fff;font-size:30px;line-height:35px}
  .panel{position:absolute;top:114px;height:637px;background:var(--panel)}
  .panel-left{left:25px;width:550px}
  .panel-right{left:618px;width:564px}

  .section-title{position:absolute;left:15px;top:13px;display:flex;align-items:center;gap:5px;
    font-family:"Roboto Condensed",sans-serif;font-weight:700;font-size:20px;color:var(--blue)}
  .section-title::before{content:"";width:14px;height:14px;background:var(--blue)}

  .gen-badge{position:absolute;width:120px;height:110px}
  .gen{position:absolute;width:170px;text-align:center}
  .gen-title{font-family:"Roboto Condensed",sans-serif;font-weight:700;color:var(--green);font-size:15px;line-height:17.5px}
  .gen-text{font-size:11.2px;line-height:15.4px;margin-top:3px}
  .dash-v{position:absolute;width:0;border-left:1px dashed var(--blue)}
  .dash-h{position:absolute;height:0;border-top:1px dashed var(--blue)}
  .divider{position:absolute;left:21px;width:510px;height:3px;background:var(--blue)}
  .rule{position:absolute;left:37px;width:489px;height:1px;background:var(--rule)}
  .lead{position:absolute;left:0;width:550px;text-align:center;font-size:14px;line-height:18px}
  .model-name{font-family:"Roboto Condensed",sans-serif;font-weight:700;color:var(--green);font-size:26px;line-height:28px}
  .model-text{font-size:11.2px;line-height:15.7px}
  .note{position:absolute;left:20px;width:510px;text-align:center;font-size:12px;line-height:15.5px}

  .ring-title{position:absolute;left:211px;width:150px;text-align:center;
    font-family:"Roboto Condensed",sans-serif;font-weight:700;color:var(--crimson);font-size:18px;line-height:21px}
  .idx-label{position:absolute;font-size:11.6px;line-height:14px}
  .idx-label.left{left:0;width:147px;text-align:right}
  .idx-num{position:absolute;font-family:"Roboto Condensed",sans-serif;font-weight:700;color:var(--crimson);font-size:21px;line-height:22px}

  .principle{position:absolute;width:255px}
  .p-num{position:absolute;left:0;top:-3px;font-family:"Roboto Condensed",sans-serif;font-weight:700;color:var(--crimson);font-size:38px;line-height:40px}
  .p-title{margin-left:40px;font-family:"Roboto Condensed",sans-serif;font-weight:700;color:var(--blue);font-size:13.5px;line-height:16.5px;white-space:nowrap}
  .p-text{margin-left:40px;margin-top:3px;width:212px;font-size:7.6px;line-height:9.2px}
  .principle.right .p-title,.principle.right .p-text{margin-left:38px}
  .principle.right .p-text{width:215px}
</style>
</head>
<body>

<div class="brand" style="left:25px;top:37px">Steady<br>Plant Works</div>
<h1 class="page-title" style="left:108px;top:32px">Reliability Centered<br>Maintenance Principles</h1>
<div class="brand" style="left:625px;top:37px">Steady<br>Plant Works</div>
<h1 class="page-title" style="left:708px;top:32px">Reliability Centered<br>Maintenance Principles</h1>

<!-- History panel -->
<section class="panel panel-left">
  <h2 class="section-title">History of Reliability Centered Maintenance</h2>

  <div class="dash-h" style="left:150px;top:99px;width:80px"></div>
  <div class="dash-h" style="left:320px;top:99px;width:90px"></div>
  <div class="dash-v" style="left:190px;top:114px;height:144px"></div>
  <div class="dash-v" style="left:356px;top:114px;height:144px"></div>

  <svg class="gen-badge" style="left:47px;top:33px" viewBox="0 0 120 110">
    <defs><path id="arc1" d="M12 66 A48 48 0 0 1 108 66"/></defs>
    <text font-family="Roboto Condensed, sans-serif" font-size="13" fill="#b91449"><textPath href="#arc1" startOffset="50%" text-anchor="middle">1st Generation</textPath></text>
    <circle cx="60" cy="66" r="34" fill="#b91449" role="img" aria-label="Steam train icon"/>
    <circle cx="60" cy="66" r="30" fill="none" stroke="#fff" stroke-width="1.2" stroke-dasharray="2 2"/>
  </svg>
  <svg class="gen-badge" style="left:215px;top:33px" viewBox="0 0 120 110">
    <defs><path id="arc2" d="M12 66 A48 48 0 0 1 108 66"/></defs>
    <text font-family="Roboto Condensed, sans-serif" font-size="13" fill="#b91449"><textPath href="#arc2" startOffset="50%" text-anchor="middle">2nd Generation</textPath></text>
    <circle cx="60" cy="66" r="34" fill="#b91449" role="img" aria-label="Tank icon"/>
    <circle cx="60" cy="66" r="30" fill="none" stroke="#fff" stroke-width="1.2" stroke-dasharray="2 2"/>
  </svg>
  <svg class="gen-badge" style="left:395px;top:33px" viewBox="0 0 120 110">
    <defs><path id="arc3" d="M12 66 A48 48 0 0 1 108 66"/></defs>
    <text font-family="Roboto Condensed, sans-serif" font-size="13" fill="#b91449"><textPath href="#arc3" startOffset="50%" text-anchor="middle">3rd Generation</textPath></text>
    <circle cx="60" cy="66" r="34" fill="#b91449" role="img" aria-label="Departing airplane icon"/>
    <circle cx="60" cy="66" r="30" fill="none" stroke="#fff" stroke-width="1.2" stroke-dasharray="2 2"/>
  </svg>

  <div class="gen" style="left:21px;top:145px">
    <div class="gen-title">Fix It<br>When It Breaks</div>
    <p class="gen-text">This made equipment<br>reliable and easy to<br>repair. And most plants<br>operated without any<br>preventive maintenance<br>in place.</p>
  </div>
  <div class="gen" style="left:190px;top:145px">
    <div class="gen-title">During<br>World War II</div>
    <p class="gen-text">Fixed interval<br>overhauls or<br>replacements to<br>prevent failures<br>became the<br>norm.</p>
  </div>
  <div class="gen" style="left:371px;top:145px">
    <div class="gen-title">More Maintenance,<br>More Failures</div>
    <p class="gen-text">Replacing<br>components before<br>they reached that<br>age would thus<br>prevent failure.</p>
  </div>

  <div class="divider" style="top:299px"></div>

  <p class="lead" style="top:320px">The move to 3rd Generation or Reliability Centered Maintenance as outlined<br>MSG-1 and MSG-2 was dramatic.</p>

  <div class="abs" style="left:8px;top:372px;width:200px;text-align:right">
    <div class="model-name">KV-3</div>
    <p class="model-text">The KV-3's maintenance schedule<br>used traditional. It required the<br>overhaul of 339 components and<br>called for more than 4,000,000<br>labour hours before reaching<br>20,000 operating hours.</p>
  </div>

  <svg class="abs" style="left:229px;top:375px;width:94px;height:94px" viewBox="0 0 94 94">
    <circle cx="47" cy="47" r="46" fill="none" stroke="#b91449" stroke-width="1.2" stroke-dasharray="2 2"/>
    <circle cx="47" cy="47" r="42" fill="#ffc000" role="img" aria-label="Airplane icon"/>
  </svg>

  <div class="abs" style="left:341px;top:372px;width:200px">
    <div class="model-name">528-400</div>
    <p class="model-text">The maintenance schedule for the<br>Arlen 528-400, developed using<br>MSG-1. It required just 66,000<br>labour hours before reaching the<br>same 20,000 operating hours!</p>
  </div>

  <div class="rule" style="top:508px"></div>
  <p class="note" style="top:522px">Another interesting comparison is to compare the number of items requiring fixed-time<br>overhauls. The maintenance for the KV-5 was developed using MSG-2 and required the<br>overhaul of just 7 items versus the 339 on the KV-3.</p>
  <div class="rule" style="top:584px"></div>
  <p class="note" style="top:596px">And both the KV-5 and Arlen 528-400 were larger and more complex than the KV-3.</p>
</section>

<!-- Principles panel -->
<section class="panel panel-right">
  <svg class="abs" style="left:0;top:0;width:564px;height:270px" viewBox="0 0 564 270" fill="none" stroke="#555" stroke-width="1" stroke-dasharray="2 2">
    <polyline points="188,34 253,34 253,80"/>
    <polyline points="188,80 204,80 204,110 228,110"/>
    <polyline points="188,127 200,127 200,140 212,140"/>
    <polyline points="188,174 200,174 200,186 225,186"/>
    <polyline points="188,234 354,234 354,214"/>
    <polyline points="378,20 310,20 310,78"/>
    <polyline points="380,89 362,89 362,110 348,110"/>
    <polyline points="380,145 362,145 362,168 350,168"/>
    <polyline points="380,212 340,212 340,200"/>
  </svg>

  <svg class="abs" style="left:210px;top:73px;width:152px;height:152px" viewBox="0 0 152 152">
    <g transform="rotate(-90 76 76)" fill="none" stroke-width="15">
      <circle cx="76" cy="76" r="68.5" stroke="#17a063" stroke-dasharray="32.5 398" stroke-dashoffset="-1.5"/>
      <circle cx="76" cy="76" r="68.5" stroke="#12a06c" stroke-dasharray="32.5 398" stroke-dashoffset="-37.4"/>
      <circle cx="76" cy="76" r="68.5" stroke="#22a466" stroke-dasharray="32.5 398" stroke-dashoffset="-73.2"/>
      <circle cx="76" cy="76" r="68.5" stroke="#47ab4d" stroke-dasharray="32.5 398" stroke-dashoffset="-109.1"/>
      <circle cx="76" cy="76" r="68.5" stroke="#86b93a" stroke-dasharray="32.5 398" stroke-dashoffset="-145"/>
      <circle cx="76" cy="76" r="68.5" stroke="#c2c42a" stroke-dasharray="32.5 398" stroke-dashoffset="-180.8"/>
      <circle cx="76" cy="76" r="68.5" stroke="#ecc41c" stroke-dasharray="32.5 398" stroke-dashoffset="-216.7"/>
      <circle cx="76" cy="76" r="68.5" stroke="#f6c019" stroke-dasharray="32.5 398" stroke-dashoffset="-252.6"/>
      <circle cx="76" cy="76" r="68.5" stroke="#f3c21c" stroke-dasharray="32.5 398" stroke-dashoffset="-288.4"/>
      <circle cx="76" cy="76" r="68.5" stroke="#dcc322" stroke-dasharray="32.5 398" stroke-dashoffset="-324.3"/>
      <circle cx="76" cy="76" r="68.5" stroke="#aabd30" stroke-dasharray="32.5 398" stroke-dashoffset="-360.2"/>
      <circle cx="76" cy="76" r="68.5" stroke="#62ae45" stroke-dasharray="32.5 398" stroke-dashoffset="-396"/>
    </g>
  </svg>
  <div class="ring-title" style="top:117px">9 Principles<br>of Modern<br>Maintenance</div>

  <p class="idx-label left" style="top:21px">Accept<br>Failures</p>
  <span class="idx-num" style="left:160px;top:26px">#1</span>
  <p class="idx-label left" style="top:67px">Most Failures Are Not<br>Age Related</p>
  <span class="idx-num" style="left:160px;top:72px">#2</span>
  <p class="idx-label left" style="top:114px">Some Failures Matter<br>More Than Others</p>
  <span class="idx-num" style="left:160px;top:118px">#3</span>
  <p class="idx-label left" style="top:161px">Parts Might Wear Out,<br>But Your Equipment<br>Breaks Down</p>
  <span class="idx-num" style="left:160px;top:165px">#4</span>
  <p class="idx-label left" style="top:222px">Hidden Failures Must<br>Be Found</p>
  <span class="idx-num" style="left:160px;top:226px">#5</span>

  <span class="idx-num" style="left:388px;top:11px">#6</span>
  <p class="idx-label" style="left:422px;top:13px">Identical Equipment<br>Does Not Mean<br>Identical<br>Maintenance</p>
  <span class="idx-num" style="left:388px;top:80px">#7</span>
  <p class="idx-label" style="left:422px;top:82px">“You Can't Maintain<br>Your Way To<br>Reliability”</p>
  <span class="idx-num" style="left:388px;top:135px">#8</span>
  <p class="idx-label" style="left:422px;top:136px">Good Maintenance<br>Programs Don't<br>Waste Your<br>Resources</p>
  <span class="idx-num" style="left:388px;top:202px">#9</span>
  <p class="idx-label" style="left:422px;top:203px">Good Maintenance<br>Programs Become<br>Better Maintenance<br>Programs</p>

  <div class="dash-v" style="left:283px;top:275px;height:358px;border-color:#777"></div>

  <article class="principle" style="left:16px;top:277px">
    <span class="p-num">#1</span>
    <h3 class="p-title">Accept&nbsp; Failures</h3>
    <p class="p-text">Not all failures can be prevented by maintenance. Some failures are the result of events outside our control. Think lightning strikes or flooding. For events like these, more or better maintenance makes no difference.</p>
  </article>
  <article class="principle" style="left:16px;top:349px">
    <span class="p-num">#2</span>
    <h3 class="p-title">Most Failures Are Not Age Related</h3>
    <p class="p-text">As explained above the research by the airline industry has shown that 70% – 90% of failure modes are not age-related. Instead, for most failure modes the likelihood of occurrence is random. Later research by the Coastal Fleet Command and others found very similar results.</p>
  </article>
  <article class="principle" style="left:16px;top:432px">
    <span class="p-num">#3</span>
    <h3 class="p-title">Some Failures Matter More Than Others</h3>
    <p class="p-text">You incur a maintenance cost in return for a benefit in sustained safety and reliability. And as with all good investments the benefit should outweigh the original investment.</p>
  </article>
  <article class="principle" style="left:16px;top:502px">
    <span class="p-num">#4</span>
    <h3 class="p-title">Parts Might Wear Out, But Your<br>Equipment Breaks Down</h3>
    <p class="p-text" style="margin-top:7px">We know the typical wear out age for a component, we can schedule a time-based task to replace it before failure.</p>
  </article>
  <article class="principle" style="left:16px;top:576px">
    <span class="p-num">#5</span>
    <h3 class="p-title">Hidden Failures Must Be Found</h3>
    <p class="p-text">Hidden failures are failures that remain undetected during normal operation. They only become evident when you need the item to work (failure on demand).</p>
  </article>

  <article class="principle right" style="left:302px;top:280px">
    <span class="p-num">#6</span>
    <h3 class="p-title">Identical Equipment Does Not Mean<br>Identical Maintenance</h3>
    <p class="p-text">The classic example is two exactly the same pumps in a duty. Both pumps process the exact same fluid under the same operating conditions. But Pump A is the duty pump, and Pump B is the standby. Pump A normally runs and Pump B is only used when Pump A fails.</p>
  </article>
  <article class="principle right" style="left:302px;top:375px">
    <span class="p-num">#7</span>
    <h3 class="p-title">“You Can't Maintain Your Way<br>To Reliability”</h3>
    <p class="p-text" style="margin-top:6px">If the equipment's inherent reliability or performance is poor, doing more maintenance will not help. No amount of maintenance can raise the inherent reliability of a design.</p>
  </article>
  <article class="principle right" style="left:302px;top:456px">
    <span class="p-num">#8</span>
    <h3 class="p-title">Good Maintenance Programs Don't<br>Waste Your Resources</h3>
    <p class="p-text" style="margin-top:6px">As maintainers we should be very careful about maintaining to design capabilities. Instead, in most cases we should maintain our equipment to deliver to operating requirements.</p>
  </article>
  <article class="principle right" style="left:302px;top:544px">
    <span class="p-num">#9</span>
    <h3 class="p-title">Good Maintenance Programs Become<br>Better Maintenance Programs</h3>
    <p class="p-text" style="margin-top:6px">The most effective maintenance programs are dynamic. They are changing and improving continuously. Always making better use of our scarce resources. Always becoming more effective at preventing those failures that matter to our business.</p>
  </article>
</section>

</body>
</html>
```